Infographics for Vextora reports

Vextora report is a summary of software developer skills.

Main purpose of our reports is to provide quick and easy insight into skill set of tested individual.
Our mission is to help talents to stand out.

Our target market is a male between 25-40, bit of a nerd, who likes technology and computer games.
The report should communicate quality and trust.

Report should fit on one A4 page and contain the following
1. Company logo - provided with the brief

2. Information about tested developer:
- Photo of developer
- Full name
- Location
- Email

3. How he or she compares against the average Software Developer:
- Collaboration ranking (0-100)
- Skills ranking by languages (up to 10 languages)

4. Total ranking - Number 1-100% which should stand out as a quick reference

We would like to included some sort of stamp of approval on the report.
The stamp would contain the overall score of a developer (The Total ranking from point 4.) .

As an option we were considering to use some sort of categorisation for the total ranking.
Here are examples of Vextora categories:
Wizard of Vextora for ranking between 90% – 100%
Scholar of Vextora for ranking between 80% - 89%
Knight of Vextora for ranking between 70% - 79%
Warrior of Vextora for ranking between 60% - 69%
Rebel of Vextora unknown or under 60%

Developer would belong to one of the categories depending on their Total ranking.

We are not very fixed on category names. We would be happy to consider any other option.

Here are some example data for the report:

The average Software Developer ranking is 50%.

Tested Developer:
Photo
Full name: Marek Tollan
Location: Sydney, Australia
Email: marek.tollan@postbox-mail.net

Collaboration ranking: 95%

Skills:
Language: C++
Number of Open Source Projects: 5
Ranking: 91%

Language: Javascript
Number of Open Source Projects: 3
Ranking: 81%

Language: Python
Number of Open Source Projects: 1
Ranking: 31%

Language: Ruby
Number of Open Source Projects: 2
Ranking: 25%

Language: C#
Ranking: 85%

Language: Java
Ranking: 75%

Total Ranking: 75% - Knight of Vextora

Thank you!

```html
<!DOCTYPE html>
<html lang="en">
<head>
<meta charset="utf-8">
<title>Vextora Report – Marek Tollan</title>
<link rel="stylesheet" href="https://fonts.googleapis.com/css2?family=Arimo:ital,wght@0,400;0,700;1,400;1,700&display=swap">
<style>
  :root {
    --plum: #8e2a76;
    --ink: #000000;
    --paper: #ffffff;
    --mist: #e3e4e6;
    --track: #d2d2d2;
    --dot-off: #d4d4d4;
  }
  * { margin: 0; padding: 0; box-sizing: border-box; }
  html, body { width: 848px; height: 1200px; overflow: hidden; background: var(--paper); }
  body { font-family: "Arimo", Arial, sans-serif; color: var(--ink); }
  .report { position: relative; width: 848px; height: 1200px; overflow: hidden; }

  /* Brand header */
  .brand { position: absolute; left: 40px; top: 58px; display: flex; align-items: center; gap: 14px; }
  .brand-square { width: 44px; height: 44px; background: var(--plum); }
  .brand-name, .brand-title { font-size: 52px; font-weight: 700; letter-spacing: -0.5px; line-height: 1; }
  .brand-divider { width: 2px; height: 50px; background: var(--ink); }

  /* Profile */
  .photo { position: absolute; left: 40px; top: 168px; width: 241px; height: 236px; background: var(--plum); }
  .profile-name { position: absolute; left: 303px; top: 176px; font-size: 50px; font-weight: 700; letter-spacing: -0.3px; }
  .profile-line { position: absolute; left: 310px; display: flex; align-items: center; gap: 12px; font-size: 24px; }
  .profile-location { top: 246px; }
  .profile-email { top: 281px; }
  .profile-email .label { color: var(--plum); font-weight: 700; }

  /* Legend band */
  .legend-band { position: absolute; left: 26px; top: 345px; width: 822px; height: 37px; background: var(--ink); }
  .legend-fold { position: absolute; left: 26px; top: 382px; }
  .legend { position: absolute; left: 300px; top: 345px; height: 37px; display: flex; align-items: center; gap: 16px; color: var(--paper); font-size: 13px; }
  .legend-item { display: flex; align-items: center; gap: 5px; }

  /* Skill rows */
  .skill { position: absolute; width: 300px; height: 100px; }
  .skill-icon { position: absolute; left: 0; top: 14px; width: 60px; height: 60px; }
  .skill-projects { position: absolute; left: 68px; top: 0; }
  .skill-count { position: absolute; right: 0; top: -2px; font-size: 31px; font-style: italic; }
  .skill-rule { position: absolute; left: 68px; right: 0; top: 40px; border-top: 2px dotted #6a6a6a; }
  .skill-ring { position: absolute; left: 68px; top: 52px; }
  .skill-score { position: absolute; right: 0; top: 50px; font-size: 31px; font-style: italic; }

  /* Collaboration seal */
  .collab-seal { position: absolute; left: 118px; top: 975px; width: 154px; height: 154px; }
  .collab-text { position: absolute; left: 118px; top: 1020px; width: 154px; text-align: center; color: var(--paper); }
  .collab-label { font-size: 12px; line-height: 1.25; }
  .collab-value { font-size: 40px; font-weight: 700; margin-top: 8px; }

  /* Total ranking */
  .rank-panel { position: absolute; left: 463px; top: 982px; width: 385px; height: 196px; background: var(--mist); }
  .rank-header { position: absolute; left: 453px; top: 952px; width: 395px; height: 31px; background: var(--plum); color: var(--paper); font-size: 17px; letter-spacing: 5px; text-align: center; line-height: 31px; font-weight: 700; }
  .rank-fold { position: absolute; left: 453px; top: 983px; }
  .rank-value { position: absolute; left: 463px; top: 990px; width: 385px; text-align: center; font-size: 168px; font-weight: 700; letter-spacing: -4px; line-height: 1.05; }

  /* Footer */
  .footer { position: absolute; left: 0; bottom: 0; width: 848px; height: 20px; background: var(--ink); color: var(--paper); font-size: 9px; display: flex; justify-content: space-between; align-items: center; padding: 0 40px; }
</style>
</head>
<body>
<main class="report">

  <header class="brand">
    <span class="brand-square"></span>
    <span class="brand-name">Vextora</span>
    <span class="brand-divider"></span>
    <span class="brand-title">Report</span>
  </header>

  <div class="photo" role="img" aria-label="Portrait photo of the developer"></div>
  <h1 class="profile-name">Marek Tollan</h1>
  <p class="profile-line profile-location">
    <svg width="16" height="24" viewBox="0 0 16 24" aria-hidden="true"><path d="M8 1C4 1 1 4 1 8c0 5 7 14 7 14s7-9 7-14c0-4-3-7-7-7z" fill="none" stroke="var(--plum)" stroke-width="2.5"/><circle cx="8" cy="8" r="2.5" fill="var(--plum)"/></svg>
    Sydney, Australia
  </p>
  <p class="profile-line profile-email"><span class="label">e:</span> marek.tollan@postbox-mail.net</p>

  <div class="legend-band"></div>
  <svg class="legend-fold" width="14" height="14" viewBox="0 0 14 14" aria-hidden="true"><polygon points="0,0 14,0 14,14" fill="#555"/></svg>
  <div class="legend">
    <span class="legend-item"><svg width="14" height="14" viewBox="0 0 14 14"><circle cx="7" cy="7" r="5" fill="none" stroke="#999" stroke-width="3"/><path d="M7 2a5 5 0 0 1 5 5" fill="none" stroke="var(--paper)" stroke-width="3"/></svg>Ranking</span>
    <span class="legend-item"><svg width="14" height="14" viewBox="0 0 14 14"><g fill="#bbb"><rect x="0" y="0" width="2" height="2"/><rect x="4" y="0" width="2" height="2"/><rect x="8" y="0" width="2" height="2"/><rect x="12" y="0" width="2" height="2"/><rect x="0" y="4" width="2" height="2"/><rect x="4" y="4" width="2" height="2"/><rect x="8" y="4" width="2" height="2"/><rect x="12" y="4" width="2" height="2"/><rect x="0" y="8" width="2" height="2"/><rect x="4" y="8" width="2" height="2"/><rect x="8" y="8" width="2" height="2"/><rect x="12" y="8" width="2" height="2"/><rect x="0" y="12" width="2" height="2"/><rect x="4" y="12" width="2" height="2"/><rect x="8" y="12" width="2" height="2"/><rect x="12" y="12" width="2" height="2"/></g></svg>Number of Projects</span>
    <span class="legend-item"><svg width="14" height="14" viewBox="0 0 14 14"><rect x="2" y="2" width="10" height="10" rx="2" transform="rotate(45 7 7)" fill="var(--plum)"/></svg>Language Skills</span>
  </div>

  <!-- Reusable symbols -->
  <svg width="0" height="0" style="position:absolute" aria-hidden="true">
    <defs>
      <symbol id="diamond" viewBox="0 0 60 60"><rect x="11" y="11" width="38" height="38" rx="4" transform="rotate(45 30 30)" fill="var(--ink)"/></symbol>
      <symbol id="dot-row-on" viewBox="0 0 28 5"><g fill="var(--plum)"><circle cx="2.5" cy="2.5" r="2.5"/><circle cx="9.5" cy="2.5" r="2.5"/><circle cx="16.5" cy="2.5" r="2.5"/><circle cx="23.5" cy="2.5" r="2.5"/></g></symbol>
      <symbol id="dot-row-off" viewBox="0 0 28 5"><g fill="var(--dot-off)"><circle cx="2.5" cy="2.5" r="2.5"/><circle cx="9.5" cy="2.5" r="2.5"/><circle cx="16.5" cy="2.5" r="2.5"/><circle cx="23.5" cy="2.5" r="2.5"/></g></symbol>
    </defs>
  </svg>

  <!-- Left column -->
  <section class="skill" style="left:113px; top:466px;">
    <svg class="skill-icon" viewBox="0 0 60 60" role="img" aria-label="C++"><use href="#diamond"/><text x="30" y="35" text-anchor="middle" font-family="Arimo, sans-serif" font-weight="700" font-size="14" fill="#fff">C++</text></svg>
    <svg class="skill-projects" width="28" height="33" viewBox="0 0 28 33" aria-label="5 projects"><use href="#dot-row-on" y="0" height="5" width="28"/><use href="#dot-row-on" y="7" height="5" width="28"/><use href="#dot-row-on" y="14" height="5" width="28"/><use href="#dot-row-on" y="21" height="5" width="28"/><use href="#dot-row-on" y="28" height="5" width="28"/></svg>
    <span class="skill-count">5</span>
    <span class="skill-rule"></span>
    <svg class="skill-ring" width="30" height="30" viewBox="0 0 30 30"><circle cx="15" cy="15" r="11" fill="none" stroke="var(--track)" stroke-width="5"/><circle cx="15" cy="15" r="11" fill="none" stroke="var(--plum)" stroke-width="5" pathLength="100" stroke-dasharray="91 100" transform="rotate(-90 15 15)"/></svg>
    <span class="skill-score">91%</span>
  </section>

  <section class="skill" style="left:113px; top:584px;">
    <svg class="skill-icon" viewBox="0 0 60 60" role="img" aria-label="Java"><use href="#diamond"/><text x="30" y="34" text-anchor="middle" font-family="Arimo, sans-serif" font-weight="700" font-size="11" fill="#fff">Java</text></svg>
    <svg class="skill-projects" width="28" height="33" viewBox="0 0 28 33" aria-label="3 projects"><use href="#dot-row-off" y="0" height="5" width="28"/><use href="#dot-row-off" y="7" height="5" width="28"/><use href="#dot-row-on" y="14" height="5" width="28"/><use href="#dot-row-on" y="21" height="5" width="28"/><use href="#dot-row-on" y="28" height="5" width="28"/></svg>
    <span class="skill-count">3</span>
    <span class="skill-rule"></span>
    <svg class="skill-ring" width="30" height="30" viewBox="0 0 30 30"><circle cx="15" cy="15" r="11" fill="none" stroke="var(--track)" stroke-width="5"/><circle cx="15" cy="15" r="11" fill="none" stroke="var(--plum)" stroke-width="5" pathLength="100" stroke-dasharray="81 100" transform="rotate(-90 15 15)"/></svg>
    <span class="skill-score">81%</span>
  </section>

  <section class="skill" style="left:113px; top:702px;">
    <svg class="skill-icon" viewBox="0 0 60 60" role="img" aria-label="Python"><use href="#diamond"/><text x="30" y="34" text-anchor="middle" font-family="Arimo, sans-serif" font-weight="700" font-size="12" fill="#fff">Py</text></svg>
    <svg class="skill-projects" width="28" height="33" viewBox="0 0 28 33" aria-label="1 project"><use href="#dot-row-off" y="0" height="5" width="28"/><use href="#dot-row-off" y="7" height="5" width="28"/><use href="#dot-row-off" y="14" height="5" width="28"/><use href="#dot-row-off" y="21" height="5" width="28"/><use href="#dot-row-on" y="28" height="5" width="28"/></svg>
    <span class="skill-count">1</span>
    <span class="skill-rule"></span>
    <svg class="skill-ring" width="30" height="30" viewBox="0 0 30 30"><circle cx="15" cy="15" r="11" fill="none" stroke="var(--track)" stroke-width="5"/><circle cx="15" cy="15" r="11" fill="none" stroke="var(--plum)" stroke-width="5" pathLength="100" stroke-dasharray="31 100" transform="rotate(-90 15 15)"/></svg>
    <span class="skill-score">31%</span>
  </section>

  <section class="skill" style="left:113px; top:822px;">
    <svg class="skill-icon" viewBox="0 0 60 60" role="img" aria-label="Ruby"><use href="#diamond"/><text x="30" y="34" text-anchor="middle" font-family="Arimo, sans-serif" font-weight="700" font-size="11" fill="#fff">Ruby</text></svg>
    <svg class="skill-projects" width="28" height="33" viewBox="0 0 28 33" aria-label="2 projects"><use href="#dot-row-off" y="0" height="5" width="28"/><use href="#dot-row-off" y="7" height="5" width="28"/><use href="#dot-row-off" y="14" height="5" width="28"/><use href="#dot-row-on" y="21" height="5" width="28"/><use href="#dot-row-on" y="28" height="5" width="28"/></svg>
    <span class="skill-count">2</span>
    <span class="skill-rule"></span>
    <svg class="skill-ring" width="30" height="30" viewBox="0 0 30 30"><circle cx="15" cy="15" r="11" fill="none" stroke="var(--track)" stroke-width="5"/><circle cx="15" cy="15" r="11" fill="none" stroke="var(--plum)" stroke-width="5" pathLength="100" stroke-dasharray="25 100" transform="rotate(-90 15 15)"/></svg>
    <span class="skill-score">25%</span>
  </section>

  <!-- Right column -->
  <section class="skill" style="left:480px; top:466px;">
    <svg class="skill-icon" viewBox="0 0 60 60" role="img" aria-label="ActionScript 3"><use href="#diamond"/><text x="30" y="34" text-anchor="middle" font-family="Arimo, sans-serif" font-weight="700" font-size="11" fill="#fff">AS3</text></svg>
    <svg class="skill-projects" width="28" height="33" viewBox="0 0 28 33" aria-label="3 projects"><use href="#dot-row-off" y="0" height="5" width="28"/><use href="#dot-row-off" y="7" height="5" width="28"/><use href="#dot-row-on" y="14" height="5" width="28"/><use href="#dot-row-on" y="21" height="5" width="28"/><use href="#dot-row-on" y="28" height="5" width="28"/></svg>
    <span class="skill-count">3</span>
    <span class="skill-rule"></span>
    <svg class="skill-ring" width="30" height="30" viewBox="0 0 30 30"><circle cx="15" cy="15" r="11" fill="none" stroke="var(--track)" stroke-width="5"/><circle cx="15" cy="15" r="11" fill="none" stroke="var(--plum)" stroke-width="5" pathLength="100" stroke-dasharray="85 100" transform="rotate(-90 15 15)"/></svg>
    <span class="skill-score">85%</span>
  </section>

  <section class="skill" style="left:480px; top:584px;">
    <svg class="skill-icon" viewBox="0 0 60 60" role="img" aria-label="JavaScript"><use href="#diamond"/><text x="30" y="36" text-anchor="middle" font-family="Arimo, sans-serif" font-weight="700" font-size="16" fill="#fff">JS</text></svg>
    <svg class="skill-projects" width="28" height="33" viewBox="0 0 28 33" aria-label="5 projects"><use href="#dot-row-on" y="0" height="5" width="28"/><use href="#dot-row-on" y="7" height="5" width="28"/><use href="#dot-row-on" y="14" height="5" width="28"/><use href="#dot-row-on" y="21" height="5" width="28"/><use href="#dot-row-on" y="28" height="5" width="28"/></svg>
    <span class="skill-count">5</span>
    <span class="skill-rule"></span>
    <svg class="skill-ring" width="30" height="30" viewBox="0 0 30 30"><circle cx="15" cy="15" r="11" fill="none" stroke="var(--track)" stroke-width="5"/><circle cx="15" cy="15" r="11" fill="none" stroke="var(--plum)" stroke-width="5" pathLength="100" stroke-dasharray="75 100" transform="rotate(-90 15 15)"/></svg>
    <span class="skill-score">75%</span>
  </section>

  <section class="skill" style="left:480px; top:702px;">
    <svg class="skill-icon" viewBox="0 0 60 60" role="img" aria-label="C"><use href="#diamond"/><text x="30" y="37" text-anchor="middle" font-family="Arimo, sans-serif" font-weight="700" font-size="20" fill="#fff">C</text></svg>
    <svg class="skill-projects" width="28" height="33" viewBox="0 0 28 33" aria-label="4 projects"><use href="#dot-row-off" y="0" height="5" width="28"/><use href="#dot-row-on" y="7" height="5" width="28"/><use href="#dot-row-on" y="14" height="5" width="28"/><use href="#dot-row-on" y="21" height="5" width="28"/><use href="#dot-row-on" y="28" height="5" width="28"/></svg>
    <span class="skill-count">4</span>
    <span class="skill-rule"></span>
    <svg class="skill-ring" width="30" height="30" viewBox="0 0 30 30"><circle cx="15" cy="15" r="11" fill="none" stroke="var(--track)" stroke-width="5"/><circle cx="15" cy="15" r="11" fill="none" stroke="var(--plum)" stroke-width="5" pathLength="100" stroke-dasharray="50 100" transform="rotate(-90 15 15)"/></svg>
    <span class="skill-score">50%</span>
  </section>

  <section class="skill" style="left:480px; top:822px;">
    <svg class="skill-icon" viewBox="0 0 60 60" role="img" aria-label="PHP"><use href="#diamond"/><text x="30" y="34" text-anchor="middle" font-family="Arimo, sans-serif" font-weight="700" font-style="italic" font-size="13" fill="#fff">php</text></svg>
    <svg class="skill-projects" width="28" height="33" viewBox="0 0 28 33" aria-label="3 projects"><use href="#dot-row-off" y="0" height="5" width="28"/><use href="#dot-row-off" y="7" height="5" width="28"/><use href="#dot-row-on" y="14" height="5" width="28"/><use href="#dot-row-on" y="21" height="5" width="28"/><use href="#dot-row-on" y="28" height="5" width="28"/></svg>
    <span class="skill-count">3</span>
    <span class="skill-rule"></span>
    <svg class="skill-ring" width="30" height="30" viewBox="0 0 30 30"><circle cx="15" cy="15" r="11" fill="none" stroke="var(--track)" stroke-width="5"/><circle cx="15" cy="15" r="11" fill="none" stroke="var(--plum)" stroke-width="5" pathLength="100" stroke-dasharray="75 100" transform="rotate(-90 15 15)"/></svg>
    <span class="skill-score">75%</span>
  </section>

  <!-- Collaboration seal -->
  <svg class="collab-seal" viewBox="-77 -77 154 154" aria-hidden="true">
    <g fill="var(--plum)">
      <circle r="62"/>
      <circle cx="62" cy="0" r="14"/><circle cx="53.7" cy="31" r="14"/><circle cx="31" cy="53.7" r="14"/>
      <circle cx="0" cy="62" r="14"/><circle cx="-31" cy="53.7" r="14"/><circle cx="-53.7" cy="31" r="14"/>
      <circle cx="-62" cy="0" r="14"/><circle cx="-53.7" cy="-31" r="14"/><circle cx="-31" cy="-53.7" r="14"/>
      <circle cx="0" cy="-62" r="14"/><circle cx="31" cy="-53.7" r="14"/><circle cx="53.7" cy="-31" r="14"/>
    </g>
  </svg>
  <div class="collab-text">
    <p class="collab-label">COLLABORATION<br>RANKING</p>
    <p class="collab-value">95%</p>
  </div>

  <!-- Total ranking -->
  <div class="rank-panel"></div>
  <div class="rank-header">KNIGHT OF VEXTORA</div>
  <svg class="rank-fold" width="10" height="10" viewBox="0 0 10 10" aria-hidden="true"><polygon points="0,0 10,0 10,10" fill="#5a1a4b"/></svg>
  <p class="rank-value">76%</p>

  <footer class="footer">
    <span>© 2014 Vextora</span>
    <span>All rights Reserved</span>
  </footer>
</main>
</body>
</html>
```